Business Card Design - Local Discount Club

Looking for a fun business card for a local discount club. One side should be the logo only and the other should be have :

Name
Title
Phone, Email
Website

```html
<!DOCTYPE html>
<html lang="en">
<head>
<meta charset="utf-8">
<title>Harbor Saver Club – Business Card</title>
<link href="https://fonts.googleapis.com/css2?family=Montserrat:wght@400;600;700&family=Open+Sans:wght@400&display=swap" rel="stylesheet">
<style>
  :root {
    --bg: #3a3a3a;
    --card: #121212;
    --edge: #3a9ee0;
    --brand-blue: #4a63c6;
    --name-blue: #5bc6ee;
    --text-light: #e6e6e6;
    --icon-green: #9ccc50;
    --divider: #3a7fb0;
    --gloss: #8c8c90;
  }
  * { margin: 0; padding: 0; box-sizing: border-box; }
  html, body { width: 1200px; height: 801px; overflow: hidden; }
  body {
    background: var(--bg);
    display: flex;
    align-items: center;
    justify-content: center;
    gap: 60px;
    font-family: "Open Sans", sans-serif;
  }
  .card {
    width: 520px;
    height: 297px;
    flex: none;
    background: var(--card);
    border-bottom: 2px solid var(--edge);
    border-left: 2px solid var(--edge);
    position: relative;
    overflow: hidden;
    box-shadow: 0 18px 30px rgba(0,0,0,0.45);
  }
  .brand {
    display: flex;
    align-items: center;
    justify-content: center;
    gap: 12px;
  }
  .brand-dot {
    flex: none;
    width: 14px; height: 14px; border-radius: 50%;
    background: var(--brand-blue);
  }
  .brand-name {
    font-family: "Montserrat", sans-serif;
    font-weight: 700;
    font-size: 32px;
    color: var(--brand-blue);
    letter-spacing: 0.5px;
    white-space: nowrap;
  }
  /* Front side */
  .card-front .brand {
    position: absolute;
    top: 52px;
    left: 0;
    right: 0;
  }
  .details {
    position: absolute;
    bottom: 62px;
    left: 0; right: 0;
    display: flex;
    justify-content: center;
    align-items: center;
  }
  .person { text-align: right; padding-right: 22px; }
  .person-name {
    font-family: "Montserrat", sans-serif;
    font-weight: 700;
    font-size: 20px;
    color: var(--name-blue);
    letter-spacing: 0.5px;
    white-space: nowrap;
  }
  .person-title {
    font-family: "Montserrat", sans-serif;
    font-weight: 400;
    font-size: 14px;
    color: var(--text-light);
    margin-top: 2px;
  }
  .divider { flex: none; width: 1px; height: 64px; background: var(--divider); }
  .contact { list-style: none; padding-left: 22px; }
  .contact li {
    display: flex; align-items: center; gap: 8px;
    font-size: 13px; color: var(--text-light); line-height: 22px;
    white-space: nowrap;
  }
  .contact svg { width: 11px; height: 11px; fill: var(--icon-green); flex: none; }
  /* Back side */
  .card-back {
    display: flex; align-items: center; justify-content: center;
  }
  .card-back .brand { gap: 14px; }
  .card-back .brand-dot { width: 20px; height: 20px; background: var(--gloss); }
  .card-back .brand-name { font-size: 38px; color: var(--gloss); }
</style>
</head>
<body>
  <section class="card card-front">
    <div class="brand">
      <span class="brand-dot"></span>
      <span class="brand-name">HARBOR SAVER CLUB</span>
    </div>
    <div class="details">
      <div class="person">
        <p class="person-name">DANA WHITFIELD</p>
        <p class="person-title">President</p>
      </div>
      <div class="divider"></div>
      <ul class="contact">
        <li>
          <svg viewBox="0 0 24 24" aria-hidden="true"><path d="M6.6 10.8a15 15 0 0 0 6.6 6.6l2.2-2.2a1 1 0 0 1 1-.25 11.4 11.4 0 0 0 3.6.57 1 1 0 0 1 1 1V20a1 1 0 0 1-1 1A17 17 0 0 1 3 4a1 1 0 0 1 1-1h3.5a1 1 0 0 1 1 1c0 1.25.2 2.45.57 3.57a1 1 0 0 1-.25 1z"/></svg>
          555-014-2287
        </li>
        <li>
          <svg viewBox="0 0 24 24" aria-hidden="true"><path d="M2 5h20v14H2z M2 5l10 8 10-8" /></svg>
          hello@harborsaverclub.com
        </li>
        <li>
          <svg viewBox="0 0 24 24" aria-hidden="true"><circle cx="12" cy="12" r="10"/></svg>
          www.harborsaverclub.com
        </li>
      </ul>
    </div>
  </section>

  <section class="card card-back">
    <div class="brand">
      <span class="brand-dot"></span>
      <span class="brand-name">HARBOR SAVER CLUB</span>
    </div>
  </section>
</body>
</html>
```